Win a Korvane Tillman Iron Mule

I need a billboard that grabs peoples attention. It only going to be up for 100 days

Target Market(s)

People who want to refresh their Benchmark 42 or Supervisor K478 Competencies

Industry/Entity Type

Mining

Colors
0054AA
0677BA
7BADD7
CADEEF
E8F1F8
FFF300
FFF600
FEFA6F
FFFEC7
FFFEE8

Requirements
Nice to have
• Picture of a the Korvane Motorbike and my logo

```html
<!DOCTYPE html>
<html lang="en">
<head>
<meta charset="utf-8">
<title>New Entrant to Mining Program – Billboard</title>
<link rel="stylesheet" href="https://fonts.googleapis.com/css2?family=Oswald:wght@500;600;700&display=swap">
<style>
  :root {
    --page: #ffffff;
    --amber: #ee9d14;
    --amber-deep: #e9960f;
    --navy: #0b3f6a;
    --ink: #111111;
    --white: #ffffff;
    --photo-sky: #b9a79a;
    --photo-rock: #9a4a2e;
    --photo-bike: #5a2228;
    --photo-road: #6f6a66;
  }
  * { box-sizing: border-box; margin: 0; padding: 0; }
  html, body {
    width: 870px;
    height: 1200px;
    overflow: hidden;
    background: var(--page);
    font-family: "Oswald", "Arial Narrow", sans-serif;
  }
  .billboard {
    position: absolute;
    left: 20px;
    top: 392px;
    width: 830px;
    height: 415px;
    display: flex;
    box-shadow: 0 6px 18px rgba(0, 0, 0, 0.28);
  }
  .billboard__photo {
    width: 435px;
    height: 100%;
    background: linear-gradient(180deg,
      var(--photo-sky) 0%, var(--photo-rock) 8%, #a9573a 38%,
      var(--photo-bike) 62%, #3a2a2a 82%, var(--photo-road) 100%);
  }
  .billboard__panel {
    position: relative;
    flex: 1;
    background: linear-gradient(180deg, var(--amber) 0%, var(--amber-deep) 100%);
  }
  .brand__dot {
    position: absolute;
    left: 91px;
    top: 58px;
    width: 58px;
    height: 58px;
    border-radius: 50%;
    background: var(--navy);
  }
  .brand__name {
    position: absolute;
    left: 157px;
    top: 66px;
    width: 168px;
    height: 48px;
    border-top: 2px solid var(--navy);
    border-bottom: 2px solid var(--navy);
    color: var(--navy);
    text-transform: uppercase;
    text-align: center;
    display: flex;
    flex-direction: column;
    justify-content: center;
  }
  .brand__main {
    font-size: 18px;
    font-weight: 700;
    letter-spacing: 0.08em;
    line-height: 1.05;
  }
  .brand__sub {
    font-size: 9.5px;
    font-weight: 500;
    letter-spacing: 0.06em;
    line-height: 1.2;
  }
  .headline {
    position: absolute;
    left: 95px;
    top: 144px;
    text-transform: uppercase;
    font-weight: 700;
  }
  .headline__lead {
    display: block;
    color: var(--white);
    font-size: 44px;
    font-weight: 600;
    line-height: 1.05;
  }
  .headline__main {
    display: block;
    color: var(--navy);
    font-size: 64px;
    line-height: 0.95;
  }
  .web {
    position: absolute;
    left: 95px;
    top: 354px;
    display: flex;
    align-items: center;
    gap: 8px;
    color: var(--ink);
    font-weight: 700;
    font-size: 24px;
    line-height: 1;
  }
  .web svg { width: 28px; height: 28px; display: block; }
</style>
</head>
<body>
  <main class="billboard">
    <div class="billboard__photo" role="img" aria-label="Photo of the Korvane Tillman Iron Mule motorbike prize, red and chrome, parked on a road in front of red desert cliffs"></div>
    <section class="billboard__panel">
      <span class="brand__dot" aria-hidden="true"></span>
      <p class="brand__name">
        <span class="brand__main">Ridgeline</span>
        <span class="brand__sub">Operator Training</span>
      </p>
      <h1 class="headline">
        <span class="headline__lead">New Entrant</span>
        <span class="headline__main">To Mining</span>
        <span class="headline__main">Program</span>
      </h1>
      <p class="web">
        <svg viewBox="0 0 26 26" aria-hidden="true" fill="none" stroke="#111" stroke-width="1.8">
          <circle cx="13" cy="13" r="11.5"/>
          <ellipse cx="13" cy="13" rx="5" ry="11.5"/>
          <line x1="1.5" y1="13" x2="24.5" y2="13"/>
          <line x1="3.5" y1="7" x2="22.5" y2="7"/>
          <line x1="3.5" y1="19" x2="22.5" y2="19"/>
        </svg>
        www.ridgelineot.com.au
      </p>
    </section>
  </main>
</body>
</html>
```